Tidal Fern Business Cards

We need something new, fun and exciting for business cards. Our current ones are just plain and we need a design that pops. We want name, position held, phone, email on the front, and a 20% discount on the back. I have also uploaded our old business cards creative to see what we are not wanting, and how boring they were and we want something jazzed up from this, cool design and catches people attention.

```html
<!DOCTYPE html>
<html lang="en">
<head>
<meta charset="utf-8">
<title>Tidal Fern Business Cards</title>
<link href="https://fonts.googleapis.com/css2?family=Montserrat:wght@400;500;600&display=swap" rel="stylesheet">
<style>
  :root {
    --backdrop: #e0e0e0;
    --card: #ffffff;
    --navy: #1b3d6e;
    --coral: #f07272;
    --blush: #f9d3d3;
    --blush-fade: rgba(249, 211, 211, 0);
  }
  html, body {
    margin: 0;
    padding: 0;
    width: 1200px;
    height: 1200px;
    overflow: hidden;
    background: var(--backdrop);
    font-family: "Montserrat", Arial, sans-serif;
  }
  .stage {
    position: relative;
    width: 1200px;
    height: 1200px;
  }
  .card {
    position: absolute;
    left: 234px;
    width: 739px;
    height: 404px;
    border-radius: 16px;
    background: var(--card);
    overflow: hidden;
    box-shadow: 0 2px 9px rgba(0, 0, 0, 0.55);
  }
  .card--front { top: 136px; }
  .card--back { top: 664px; }
  .card svg {
    position: absolute;
    inset: 0;
    width: 739px;
    height: 404px;
    display: block;
  }
  .brand-name {
    font-family: "Montserrat", Arial, sans-serif;
    font-weight: 600;
    fill: var(--navy);
  }
  .contact-text {
    font-family: "Montserrat", Arial, sans-serif;
    font-weight: 400;
    font-size: 31px;
    fill: var(--coral);
  }
  .icon {
    fill: none;
    stroke: var(--coral);
    stroke-width: 1.4;
    stroke-linecap: round;
    stroke-linejoin: round;
  }
  .tagline {
    font-family: "Montserrat", Arial, sans-serif;
    font-weight: 500;
    font-size: 24px;
    letter-spacing: 9px;
    fill: var(--navy);
  }
  .offer-frame {
    fill: none;
    stroke: var(--coral);
    stroke-width: 3;
  }
  .offer-value {
    font-family: "Montserrat", Arial, sans-serif;
    font-weight: 400;
    font-size: 58px;
    letter-spacing: -2px;
    fill: var(--coral);
  }
  .offer-label {
    font-family: "Montserrat", Arial, sans-serif;
    font-weight: 400;
    font-size: 30px;
    letter-spacing: -1.5px;
    fill: var(--coral);
  }
</style>
</head>
<body>
<main class="stage">

  <!-- Front: name and contact details -->
  <section class="card card--front" aria-label="Business card front">
    <svg viewBox="0 0 739 404" xmlns="http://www.w3.org/2000/svg">
      <defs>
        <radialGradient id="blush-glow">
          <stop offset="0" stop-color="var(--blush)" stop-opacity="0.85"/>
          <stop offset="1" stop-color="var(--blush)" stop-opacity="0"/>
        </radialGradient>
      </defs>

      <g class="decor" role="img" aria-label="Soft blush floral motif in the background">
        <ellipse cx="170" cy="60" rx="190" ry="120" fill="url(#blush-glow)"/>
        <ellipse cx="90" cy="320" rx="150" ry="110" fill="url(#blush-glow)"/>
        <ellipse cx="360" cy="330" rx="120" ry="90" fill="url(#blush-glow)"/>
        <ellipse cx="710" cy="90" rx="90" ry="100" fill="url(#blush-glow)"/>
      </g>

      <g class="brand" aria-label="Tidal Fern">
        <circle cx="149" cy="55" r="15" fill="var(--coral)"/>
        <text class="brand-name" x="24" y="156" font-size="50">Tidal Fern</text>
      </g>

      <path class="contact-panel" fill="var(--navy)"
            d="M739 202 L739 404 L387 404 C380 300 470 205 640 196 C690 194 720 198 739 202 Z"/>

      <g class="contact-list">
        <g class="icon icon--phone" transform="translate(469 271)">
          <path d="M3 3 C1 5 1 9 5 14 C9 19 14 21 17 19 L19 17 L15 13 L12 15 C10 14 7 11 6 9 L8 6 L4 2 Z"/>
          <path d="M13 2 A8 8 0 0 1 20 9"/>
          <path d="M13 5 A5 5 0 0 1 17 9"/>
        </g>
        <text class="contact-text" x="507" y="288">phone</text>

        <g class="icon icon--pin" transform="translate(473 305)">
          <path d="M8 22 C8 22 1 13 1 8 A7 7 0 0 1 15 8 C15 13 8 22 8 22 Z"/>
          <circle cx="8" cy="8" r="3"/>
          <path d="M3 25 H13"/>
        </g>
        <text class="contact-text" x="507" y="327">position held</text>

        <g class="icon icon--mail" transform="translate(469 347)">
          <path d="M1 8 L11 1 L21 8 V20 H1 Z"/>
          <path d="M1 8 L11 15 L21 8"/>
          <path d="M1 20 L8 13 M21 20 L14 13"/>
          <path d="M5 10 V4 H17 V10"/>
        </g>
        <text class="contact-text" x="507" y="366">E mail</text>
      </g>
    </svg>
  </section>

  <!-- Back: tagline, name and discount offer -->
  <section class="card card--back" aria-label="Business card back">
    <svg viewBox="0 0 739 404" xmlns="http://www.w3.org/2000/svg">
      <defs>
        <radialGradient id="blush-glow-back">
          <stop offset="0" stop-color="var(--blush)" stop-opacity="0.9"/>
          <stop offset="1" stop-color="var(--blush)" stop-opacity="0"/>
        </radialGradient>
        <path id="tagline-arc" d="M135 223 A100 100 0 1 1 315 223"/>
      </defs>

      <g class="decor" role="img" aria-label="Soft blush floral motif in the background">
        <ellipse cx="60" cy="80" rx="130" ry="150" fill="url(#blush-glow-back)"/>
        <ellipse cx="390" cy="360" rx="120" ry="80" fill="url(#blush-glow-back)"/>
      </g>

      <path class="offer-panel" fill="var(--navy)"
            d="M388 0 L739 0 L739 404 L630 404 C500 395 420 260 388 0 Z"/>

      <text class="tagline">
        <textPath href="#tagline-arc" startOffset="50%" text-anchor="middle">BE CALM, GROW</textPath>
      </text>

      <g class="brand" aria-label="Tidal Fern">
        <circle cx="225" cy="182" r="22" fill="var(--coral)"/>
        <text class="brand-name" x="224" y="298" font-size="48" text-anchor="middle">Tidal Fern</text>
      </g>

      <g class="offer">
        <rect class="offer-frame" x="515" y="120" width="168" height="147" rx="24"/>
        <text class="offer-value" x="599" y="204" text-anchor="middle">20%</text>
        <text class="offer-label" x="599" y="237" text-anchor="middle">Discount</text>
      </g>
    </svg>
  </section>

</main>
</body>
</html>
```